MODELS AGENCY NEW YEAR 2026 CARD

A 10 cm x 21 cm horizontal New Year card for clients of our 2 models agencies, Pommelin (kids) and Velvaride (actors and adults) (logo in the jobs).

Side A of the card: creative mission:
-text: 2026
-text: Peace and Love
-Studio or movie set atmosphere
-tone of voice: optimistic, positive, colorful

Side B:
(name of 4 people of the agency:)
Odette, Anne-Sophie, Hortense & Luc-Antoine,
(2 logos)
Pommelin & VelvaRide
(Adres)
Rue des Tilleuls 74 b3 - 1200 Bruxelles - Belgique

Target Market(s)

Movie directors, photographers

Industry/Entity Type

Fashion, advertising & Movies

Requirements
Must have
• SEE TEXT IN BRIEFING

```html
<!DOCTYPE html>
<html lang="en">
<head>
<meta charset="utf-8">
<title>Pommelin &amp; Velvaride — New Year 2026 Card</title>
<link rel="stylesheet" href="https://fonts.googleapis.com/css2?family=Barlow:wght@400;500;600;800&family=Pinyon+Script&display=swap">
<style>
  :root {
    --backdrop: #e8dfc4;
    --card-white: #ffffff;
    --ink-purple: #3b1e5a;
    --kids-blue: #18a3e0;
    --adults-orange: #f06423;
    --number-mint: #e6f4ef;
    --title-white: #ffffff;
  }
  * { box-sizing: border-box; margin: 0; padding: 0; }
  html, body {
    width: 1200px; height: 1029px; overflow: hidden;
    background: var(--backdrop);
    font-family: "Barlow", Arial, sans-serif;
  }
  .sheet { position: relative; width: 1200px; height: 1029px; }

  .card-side {
    position: absolute; left: 175px; width: 850px; height: 405px;
    box-shadow: 14px 18px 30px rgba(120, 100, 60, 0.18);
    overflow: hidden;
  }
  .side-front { top: 79px; }
  .side-back { top: 554px; background: var(--card-white); }

  .studio-photo {
    position: absolute; inset: 0;
    background:
      linear-gradient(90deg, rgba(40,40,45,0.85) 0%, rgba(40,40,45,0.2) 20%, rgba(0,0,0,0) 28%),
      linear-gradient(110deg, #c42a5e 0%, #22b7c9 30%, #e58aa3 52%, #f0b02e 72%, #d9335f 100%);
  }
  .front-title {
    position: absolute; top: 100px; left: 0; width: 100%;
    text-align: center; transform: translateY(-50%);
    color: var(--title-white);
    font-weight: 600; font-size: 36px; letter-spacing: 6px;
    text-shadow: 2px 3px 6px rgba(0,0,0,0.35);
  }
  .front-year {
    position: absolute; left: 0; width: 100%; top: 200px;
    text-align: center;
    color: var(--number-mint);
    font-weight: 800; font-size: 200px; line-height: 1; letter-spacing: -4px;
    text-shadow: 6px 8px 10px rgba(120,40,80,0.35);
  }

  .agency-block {
    position: absolute; top: 150px; width: 240px;
    text-align: center; color: var(--ink-purple);
  }
  .agency-kids { left: 44px; }
  .agency-adults { left: 568px; }
  .agency-name {
    display: inline-flex; align-items: center; gap: 10px;
    font-weight: 800; font-size: 38px; line-height: 1;
    color: var(--ink-purple);
  }
  .agency-dot { width: 14px; height: 14px; border-radius: 50%; }
  .agency-kids .agency-dot { background: var(--kids-blue); }
  .agency-adults .agency-dot { background: var(--adults-orange); }
  .agency-tagline {
    margin-top: 10px; font-size: 12.5px; letter-spacing: 1.5px;
  }
  .agency-since {
    margin-top: 44px; font-size: 9px; letter-spacing: 0.5px;
  }
  .agency-kids .agency-since { color: var(--kids-blue); }
  .agency-adults .agency-since { color: var(--adults-orange); }

  .team-names {
    position: absolute; top: 115px; left: 300px; width: 260px;
    text-align: center; color: var(--ink-purple);
    font-family: "Pinyon Script", cursive;
    font-size: 26px; line-height: 35px;
  }

  .contact-line {
    position: absolute; top: 353px; font-size: 15px; white-space: nowrap;
  }
  .phone-kids { left: 97px; color: var(--kids-blue); }
  .address { left: 257px; color: var(--ink-purple); }
  .phone-adults { left: 630px; color: var(--adults-orange); }
</style>
</head>
<body>
<main class="sheet">
  <section class="card-side side-front">
    <div class="studio-photo" role="img" aria-label="Photo studio scene with softbox lights and a camera, four smiling young adults among confetti in front of a colourful geometric backdrop"></div>
    <h1 class="front-title">Peace and Love</h1>
    <div class="front-year">2026</div>
  </section>

  <section class="card-side side-back">
    <div class="agency-block agency-kids">
      <div class="agency-name"><span class="agency-dot"></span>Pommelin</div>
      <p class="agency-tagline">CHILDREN MODELS AGENCY</p>
      <p class="agency-since">– SINCE 1982 –</p>
    </div>

    <p class="team-names">Odette,<br>Anne-Sophie,<br>Hortense<br>&amp; Luc-Antoine</p>

    <div class="agency-block agency-adults">
      <div class="agency-name"><span class="agency-dot"></span>VelvaRide</div>
      <p class="agency-tagline">PEOPLE, ACTORS &amp; MODELS AGENCY</p>
      <p class="agency-since">– SINCE 2000 –</p>
    </div>

    <p class="contact-line phone-kids">+32 (0) 2 318 52 74</p>
    <p class="contact-line address">Rue des Tilleuls 74 b3 - 1200 Bruxelles - Belgique</p>
    <p class="contact-line phone-adults">+32 (0) 2 318 66 19</p>
  </section>
</main>
</body>
</html>
```